jewelry,purses,pj's,and retro bathing caps

I need a business card to hand out to people because i wear my jewelry and also to put in box with purchases. I want a card with maybe me as a redhead covered in jewelry carrying an overflowing shopping bag.
Target Market(s)
my tradlo customers and people on the street who compliment me about my jewelry
Industry/Entity Type
Shopping
Contact Information for Business Card
glimmerboutique4719
This is my Tradlo Store
we guarantee happiness or money back
Font styles to use
Serif
Requirements
Must have
- pix of jewelry on a mannequin
the fact that I am a "crest lister"

```html
<!DOCTYPE html>
<html lang="en">
<head>
<meta charset="UTF-8">
<title>Glimmer Boutique Business Card</title>
<link rel="stylesheet" href="https://fonts.googleapis.com/css2?family=Didact+Gothic&display=swap">
<style>
  :root {
    --page-bg: #d4d4d4;
    --card-bg: #000000;
    --accent-pink: #e8336d;
    --text-light: #f2f2f2;
    --text-muted: #bdbdbd;
    --photo-dark: #111111;
    --photo-mid: #4a4a4a;
    --photo-pearl: #d9d9d9;
  }
  html, body {
    margin: 0;
    padding: 0;
    width: 1200px;
    height: 1200px;
    overflow: hidden;
    background: var(--page-bg);
  }
  .business-card {
    position: absolute;
    left: 60px;
    top: 285px;
    width: 1080px;
    height: 630px;
    background: var(--card-bg);
    overflow: hidden;
    font-family: "Didact Gothic", "Century Gothic", sans-serif;
  }
  .jewelry-photo {
    position: absolute;
    left: 0;
    top: 0;
    width: 540px;
    height: 630px;
    background:
      radial-gradient(ellipse 42% 62% at 42% 42%, var(--photo-pearl) 0%, #9a9a9a 30%, var(--photo-mid) 55%, rgba(20,20,20,0) 85%),
      radial-gradient(ellipse 30% 40% at 8% 25%, #8a8a8a 0%, rgba(40,40,40,0) 80%),
      linear-gradient(90deg, var(--photo-dark) 0%, #1c1c1c 45%, var(--card-bg) 100%);
  }
  .brand-rule {
    position: absolute;
    left: 514px;
    top: 119px;
    width: 372px;
    height: 3px;
    background: var(--accent-pink);
  }
  .marketplace-name {
    position: absolute;
    right: 56px;
    top: 94px;
    margin: 0;
    font-size: 44px;
    line-height: 1;
    color: var(--text-light);
  }
  .store-name {
    position: absolute;
    right: 56px;
    top: 156px;
    margin: 0;
    font-size: 44px;
    font-weight: 400;
    line-height: 1;
    color: var(--text-light);
    letter-spacing: 0.5px;
  }
  .seller-status {
    position: absolute;
    right: 56px;
    top: 220px;
    margin: 0;
    font-size: 24px;
    line-height: 1;
    color: var(--text-muted);
    letter-spacing: 1px;
  }
  .guarantee-tagline {
    position: absolute;
    right: 52px;
    top: 480px;
    margin: 0;
    font-size: 28px;
    line-height: 1;
    color: var(--accent-pink);
    letter-spacing: 0.4px;
  }
</style>
</head>
<body>
  <main class="business-card">
    <div class="jewelry-photo" role="img" aria-label="Photo of a white bubble statement necklace on a black sequined mannequin"></div>
    <div class="brand-rule"></div>
    <p class="marketplace-name">tradlo</p>
    <h1 class="store-name">glimmerboutique4719</h1>
    <p class="seller-status">crest lister</p>
    <p class="guarantee-tagline">We guarantee happiness or money back</p>
  </main>
</body>
</html>
```